Digital Album Cover - Piano music for wedding ceremonies and receptions

I need cover art for a piano album project that will be distributed to TuneVault, Wavelane etc. Covert art required for front of album. At this stage physical CDs will not be printed nor required it is just a digital release.
Artist name: Toby Hargrove
Album Title: Gentle Keys Melodies Wedding Ceremonies and Receptions
Volume 3
Sample piano songs are on my tunecast page
https://tunecast.example/tobyhargrovekeys/sets/gentle-keys-melodies-vol-3
Previous album artwork used from sketch hive competitions winners
https://musicvault.example/au/artist/toby-hargrove/4830917265
Target Market(s)
brides to be
grooms to be
people interested in weddings
people enjoy love songs or easy listening music
Industry/Entity Type
Wedding
Look and feel
Each slider illustrates characteristics of the customer's brand and the style your logo design should communicate.

```html
<!DOCTYPE html>
<html lang="en">
<head>
<meta charset="utf-8">
<title>Toby Hargrove – Gentle Keys Melodies Volume 3</title>
<link rel="stylesheet" href="https://fonts.googleapis.com/css2?family=Montserrat:wght@800&family=Raleway:wght@400;500;700&display=swap">
<style>
  :root {
    --sky-deep: #0c0b22;
    --sky-mid: #1d1a4e;
    --sky-glow: #3f3a96;
    --frame: #ffffff;
    --numeral: #9a98a8;
    --volume: #6e97a1;
    --artist: #f4f6fa;
    --subtitle: #a9c4cb;
  }
  html, body {
    margin: 0;
    padding: 0;
    width: 1200px;
    height: 1200px;
    overflow: hidden;
    background: #ffffff;
  }
  .album-cover {
    display: block;
    width: 1200px;
    height: 1200px;
  }
  .volume-numeral {
    font-family: "Montserrat", sans-serif;
    font-weight: 800;
    font-size: 640px;
    fill: var(--numeral);
    fill-opacity: 0.82;
  }
  .volume-label {
    font-family: "Raleway", sans-serif;
    font-weight: 500;
    font-size: 80px;
    fill: var(--volume);
  }
  .artist-name {
    font-family: "Raleway", sans-serif;
    font-weight: 700;
    font-size: 66px;
    letter-spacing: 0.2em;
    fill: var(--artist);
  }
  .album-title {
    font-family: "Raleway", sans-serif;
    font-weight: 400;
    font-size: 35px;
    fill: var(--subtitle);
  }
</style>
</head>
<body>
<svg class="album-cover" viewBox="0 0 1200 1200" xmlns="http://www.w3.org/2000/svg">
  <defs>
    <linearGradient id="sky-base" x1="0" y1="0" x2="1" y2="1">
      <stop offset="0" stop-color="var(--sky-deep)"/>
      <stop offset="0.55" stop-color="var(--sky-mid)"/>
      <stop offset="1" stop-color="var(--sky-deep)"/>
    </linearGradient>
    <radialGradient id="galaxy-band" cx="0.72" cy="0.45" r="0.55">
      <stop offset="0" stop-color="var(--sky-glow)" stop-opacity="0.75"/>
      <stop offset="1" stop-color="var(--sky-glow)" stop-opacity="0"/>
    </radialGradient>
  </defs>

  <g class="night-sky" role="img" aria-label="Photograph of a starry night sky with the Milky Way crossing diagonally">
    <rect width="1200" height="1200" fill="url(#sky-base)"/>
    <rect width="1200" height="1200" fill="url(#galaxy-band)"/>
  </g>

  <rect class="inner-frame" x="43" y="43" width="1114" height="1114" fill="none" stroke="var(--frame)" stroke-width="3"/>

  <text class="volume-numeral" x="752" y="1096">3</text>
  <text class="volume-label" x="577" y="871">Volume</text>
  <text class="artist-name" x="195" y="947">Toby Hargrove</text>
  <text class="album-title" x="195" y="1015">Gentle Keys Melodies Wedding</text>
  <text class="album-title" x="195" y="1063">Ceremonies and Receptions</text>
</svg>
</body>
</html>
```